Website Design - Financial Services Software

We are looking for website designs for our public website.
Some competitor sites we like are
www.torvani.com.au
www.pluma.com.au
www.quentabridge.com
www.morlupa.com.au

A wireframe example of our site can be found at
http://pr4tqz.bivlowpage.com/

Attached is our logo.

Industry/Entity Type

Financial

```html
<!DOCTYPE html>
<html lang="en">
<head>
<meta charset="utf-8">
<title>Corvessa – Smarter Financial Strategies</title>
<link href="https://fonts.googleapis.com/css2?family=Open+Sans:wght@400;600&family=Tinos&display=swap" rel="stylesheet">
<style>
:root{
  --brown:#774104;
  --brown-dark:#5e3303;
  --gold-top:#a8691c;
  --gold-bottom:#d9a445;
  --blue:#1170c8;
  --blue-band:#1371c6;
  --dark:#333333;
  --black:#050505;
  --text:#2b2b2b;
  --white:#ffffff;
  --line:#555555;
}
*{margin:0;padding:0;box-sizing:border-box}
html,body{width:1200px;height:1151px;overflow:hidden;background:var(--white)}
body{font-family:"Open Sans",Arial,sans-serif;color:var(--text);position:relative}
.page{position:relative;width:1200px;height:1151px;overflow:hidden}
.abs{position:absolute}

.top-rule{left:0;top:0;width:1200px;height:3px;background:var(--brown)}

.brand{left:200px;top:20px;width:120px;text-align:center}
.brand-mark{width:54px;height:54px;margin:0 auto 6px;background:var(--gold-top);border-radius:4px}
.brand-name{font-family:"Tinos",serif;font-size:23px;color:#b87f2a;letter-spacing:1px;line-height:1}
.brand-tag{font-family:"Tinos",serif;font-size:7px;color:#555;letter-spacing:.3px;margin-top:2px}

.btn-account{top:28px;height:28px;width:84px;background:var(--blue);color:var(--white);border-radius:3px;font-size:12px;display:flex;align-items:center;justify-content:center}
.nav-item{top:91px;height:28px;width:84px;border-radius:4px;background:linear-gradient(var(--gold-top),var(--gold-bottom));color:var(--white);font-size:13px;font-weight:600;display:flex;align-items:center;justify-content:center}

.hero{left:0;top:135px;width:1200px;height:441px;background:linear-gradient(90deg,#b9b7b4 0%,#8d8579 30%,#6b6256 55%,#3a3f55 78%,#8a8789 100%)}
.hero-title{left:198px;top:218px;font-family:"Tinos",serif;font-size:31px;color:var(--white);text-shadow:0 1px 3px rgba(0,0,0,.6)}
.hero-sub{left:200px;top:270px;width:380px;font-size:21px;line-height:24px;color:var(--white);text-shadow:0 1px 3px rgba(0,0,0,.6)}
.audience{top:342px;width:174px;height:138px;border:1px solid #ddd;background:#c9c7c4}
.audience-photo{width:100%;height:106px}
.audience-label{height:31px;background:#c8c8c8;display:flex;align-items:center;justify-content:center;font-size:12.5px;color:#555}
.play{left:598px;top:309px}

.intro-title{left:198px;top:608px;font-family:"Tinos",serif;font-size:33px;color:var(--brown)}
.intro-text{left:198px;width:362px;font-size:11.5px;line-height:16px;color:var(--text)}

.tile{width:128px;height:86px;border-radius:3px;background:var(--brown);color:var(--white);font-size:13px;font-weight:600;line-height:13px;text-align:center;display:flex;flex-direction:column;align-items:center;justify-content:center;gap:6px}
.tile.active{background:var(--blue)}

.cta-band{left:0;top:847px;width:1200px;height:97px;background:var(--blue-band)}
.cta-text{left:198px;top:880px;font-family:"Tinos",serif;font-size:23px;color:var(--white)}
.cta-btn{left:692px;top:876px;width:308px;height:40px;border-radius:2px;background:linear-gradient(#8a4a05,#6c3903);font-family:"Tinos",serif;font-size:20px;color:var(--white);display:flex;align-items:center;justify-content:center}

.footer{left:0;top:944px;width:1200px;height:174px;background:var(--dark)}
.footer-brand{left:200px;top:991px;width:117px;height:94px;background:#000;display:flex;flex-direction:column;align-items:center;justify-content:center;gap:4px}
.footer-brand .mark{width:30px;height:30px;background:#ddd;border-radius:3px}
.footer-brand .name{font-family:"Tinos",serif;font-size:14px;color:var(--white);letter-spacing:.5px}
.footer-head{top:995px;font-family:"Tinos",serif;font-size:15px;color:#ddd}
.footer-rule{top:1019px;height:1px;background:var(--line)}
.footer-links{top:1030px;list-style:none;font-size:11.5px;line-height:20px;color:#e6e6e6}
.footer-links li{display:flex;align-items:center;gap:5px}
.social-dot{width:10px;height:10px;background:#e6e6e6;border-radius:1px}

.legal-bar{left:0;top:1118px;width:1200px;height:33px;background:var(--black)}
.copyright{left:199px;top:1127px;font-size:9.5px;color:#e6e6e6}
</style>
</head>
<body>
<div class="page">
  <div class="abs top-rule"></div>

  <header>
    <div class="abs brand">
      <div class="brand-mark"></div>
      <div class="brand-name">CORVESSA</div>
      <div class="brand-tag">SMARTER FINANCIAL STRATEGIES</div>
    </div>
    <a class="abs btn-account" style="left:830px">Sign up</a>
    <a class="abs btn-account" style="left:918px">Login</a>
    <nav>
      <a class="abs nav-item" style="left:562px">Home</a>
      <a class="abs nav-item" style="left:651px">Features</a>
      <a class="abs nav-item" style="left:740px">FAQ</a>
      <a class="abs nav-item" style="left:829px">About</a>
      <a class="abs nav-item" style="left:918px">Examples</a>
    </nav>
  </header>

  <section>
    <div class="abs hero" role="img" aria-label="Video still of two financial advisers in an office meeting, one holding a tablet"></div>
    <h1 class="abs hero-title">Smarter Financial Strategies</h1>
    <p class="abs hero-sub">Values and Cash-flow focused fiancial software for financial planners</p>
    <div class="abs audience" style="left:202px">
      <div class="audience-photo" role="img" aria-label="Hands reviewing a financial document with a pen" style="background:linear-gradient(#6a5c52,#d9d6d0)"></div>
      <div class="audience-label">For planing Practices</div>
    </div>
    <div class="abs audience" style="left:387px">
      <div class="audience-photo" role="img" aria-label="Group of business people standing in front of a bridge" style="background:linear-gradient(#8e99a8,#3a3536)"></div>
      <div class="audience-label">For Dealer Groups</div>
    </div>
    <svg class="abs play" width="68" height="68" viewBox="0 0 68 68" aria-label="Play video">
      <circle cx="34" cy="34" r="31" fill="#222" stroke="#fff" stroke-width="4"/>
      <path d="M26 20 L48 34 L26 48 Z" fill="#fff"/>
    </svg>
  </section>

  <section>
    <h2 class="abs intro-title">Lorem Ipsum is simply</h2>
    <p class="abs intro-text" style="top:657px">Lorem Ipsum is simply dummy text of the printing and typesetting industry. Lorem Ipsum has been the industry's standard dummy text ever since the 1500s, when an unknown printer took a galley of type and scrambled it to make a type specimen book.</p>
    <p class="abs intro-text" style="top:737px">It has survived not only five centuries, but also the leap into electro-nic typesetting, remaining essentially unchanged. It was popularised in the 1960s with the release of Typeline sheets containing Lorem Ipsum passages,</p>

    <div class="abs tile active" style="left:603px;top:622px">
      <svg width="16" height="16" viewBox="0 0 16 16"><circle cx="9.5" cy="6.5" r="4.5" fill="none" stroke="#fff" stroke-width="2"/><path d="M6 10 L2 14" stroke="#fff" stroke-width="2.4"/></svg>
      <span>Fact Find</span>
    </div>
    <div class="abs tile" style="left:738px;top:622px">
      <svg width="16" height="16" viewBox="0 0 16 16"><path d="M3 1h7l3 3v11H3z" fill="none" stroke="#fff" stroke-width="1.5"/><circle cx="10" cy="11" r="3" fill="#fff"/></svg>
      <span>Online data</span>
    </div>
    <div class="abs tile" style="left:873px;top:622px">
      <svg width="18" height="16" viewBox="0 0 18 16"><path d="M1 8v7h15" fill="none" stroke="#fff" stroke-width="1.5"/><path d="M6 12 L15 3 L17 5 L8 14 Z" fill="#fff"/></svg>
      <span>Custom<br>Branding</span>
    </div>
    <div class="abs tile" style="left:603px;top:715px">
      <svg width="16" height="16" viewBox="0 0 16 16" fill="#fff"><rect x="5" y="1" width="6" height="4"/><rect x="1" y="10" width="5" height="4"/><rect x="10" y="10" width="5" height="4"/><path d="M3 10V7h10v3M8 5v2" stroke="#fff" stroke-width="1.3" fill="none"/></svg>
      <span>Site<br>Intigration</span>
    </div>
    <div class="abs tile" style="left:738px;top:715px">
      <svg width="16" height="16" viewBox="0 0 16 16"><path d="M8 2 L4 6h3v5h2V6h3z M2 11v3h12v-3" fill="#fff" stroke="#fff" stroke-width="1"/></svg>
      <span>Upload File</span>
    </div>
    <div class="abs tile" style="left:873px;top:715px">
      <svg width="16" height="16" viewBox="0 0 16 16" fill="#fff"><circle cx="8" cy="5" r="4"/><path d="M1 16c0-5 3-6 7-6s7 1 7 6z"/></svg>
      <span>User<br>Management</span>
    </div>
  </section>

  <section>
    <div class="abs cta-band"></div>
    <p class="abs cta-text">Create an account today and begin your 30 day trial!</p>
    <a class="abs cta-btn">Sign up Now!</a>
  </section>

  <footer>
    <div class="abs footer"></div>
    <div class="abs footer-brand"><div class="mark"></div><div class="name">CORVESSA</div></div>

    <h3 class="abs footer-head" style="left:366px">About us</h3>
    <div class="abs footer-rule" style="left:361px;width:100px"></div>
    <ul class="abs footer-links" style="left:366px"><li>About us</li><li>Support</li></ul>

    <h3 class="abs footer-head" style="left:528px">Getting Started</h3>
    <div class="abs footer-rule" style="left:524px;width:145px"></div>
    <ul class="abs footer-links" style="left:530px"><li>Why Corvessa</li><li>Download a Summary</li><li>Corvessa Videos</li></ul>

    <h3 class="abs footer-head" style="left:726px">Legal</h3>
    <div class="abs footer-rule" style="left:722px;width:114px"></div>
    <ul class="abs footer-links" style="left:726px"><li>Terms of Use</li><li>Privacy</li></ul>

    <h3 class="abs footer-head" style="left:874px">Connect</h3>
    <div class="abs footer-rule" style="left:870px;width:131px"></div>
    <ul class="abs footer-links" style="left:874px"><li><span class="social-dot"></span>Corvessa on Linkora</li><li><span class="social-dot"></span>Corvessa on Chirpline</li></ul>

    <div class="abs legal-bar"></div>
    <p class="abs copyright">Copyright © 2014 Corvessa Pty Ltd. All rights reserved.</p>
  </footer>
</div>
</body>
</html>
```